A small electrical company designed a vehicle wrap for the Corvan Haulmark 360

We designed a vehicle wrap for a small Los Angeles electrical company specializing in electrical repairs, air conditioning repair and installation, electric vehicle charging station installation, and electrical upgrades. Our clientele primarily serves residential and commercial customers. To stay within our budget, we chose a clear, eye-catching electrical and air conditioning logo that combined fonts and graphics to create a memorable impression.
Target Market(s)
electrical repair & installation, cooling&heating ,EV charger installation
Industry/Entity Type
electrical and Air conditioning
Requirements
Must have
- phone number:(555)4820173 Lic#:2048736 website www.quorvelectric.example
Nice to have
- my vehicle is Corvan haulmark 360 high roof 148'WB cargo van

```html
<!DOCTYPE html>
<html lang="en">
<head>
<meta charset="utf-8">
<title>Quorv Electric Solution Inc — Corvan Haulmark 360 wrap concepts</title>
<link href="https://fonts.googleapis.com/css2?family=Oswald:wght@500&family=Roboto+Condensed:wght@700&family=Noto+Serif:ital@1&display=swap" rel="stylesheet">
<style>
  :root {
    --navy: #22304a;
    --orange: #ef9a25;
    --white: #ffffff;
    --body: #f3f4f5;
    --glass: #3d4148;
    --tyre: #1d1e21;
    --trim: #2a2b2e;
  }
  html, body { margin: 0; padding: 0; overflow: hidden; }
  body { width: 1200px; height: 1200px; background: var(--white); }
  .wrap-sheet { display: block; width: 1200px; height: 1200px; }
  .van-body { fill: var(--body); stroke: #d6d8db; stroke-width: 1; }
  .van-glass { fill: var(--glass); }
  .van-trim { fill: var(--trim); }
  .van-tyre { fill: var(--tyre); }
  .van-hub { fill: #9a9da2; }
  .fill-navy { fill: var(--navy); }
  .fill-orange { fill: var(--orange); }
  .fill-white { fill: var(--white); }
  .company-name { font-family: 'Oswald', sans-serif; font-weight: 500; fill: var(--navy); }
  .website { font-family: 'Roboto Condensed', sans-serif; font-weight: 700; }
  .tagline { font-family: 'Noto Serif', serif; font-style: italic; fill: var(--orange); }
  .services { font-family: 'Roboto Condensed', sans-serif; font-weight: 700; fill: var(--white); }
  .licence { font-family: 'Roboto Condensed', sans-serif; font-weight: 700; }
  .phone { font-family: 'Roboto Condensed', sans-serif; font-weight: 700; }
  .rule { stroke: var(--orange); stroke-width: 1.2; }
</style>
</head>
<body>
<svg class="wrap-sheet" viewBox="0 0 960 960" xmlns="http://www.w3.org/2000/svg" aria-label="Three side-view wrap concepts for the Corvan Haulmark 360 van">
  <defs>
    <path id="van-outline" d="M188,274 L186,92 Q186,64 214,64 L560,62 Q600,62 640,100 L700,160 Q770,180 790,210 L798,274 Z"/>
    <clipPath id="van-clip"><use href="#van-outline"/></clipPath>
    <g id="van-chassis">
      <path class="van-glass" d="M604,128 L650,128 L692,172 L694,198 L604,198 Z"/>
      <path class="van-trim" d="M186,252 L798,252 L798,274 L186,274 Z"/>
      <circle class="van-tyre" cx="357" cy="282" r="30"/><circle class="van-hub" cx="357" cy="282" r="13"/>
      <circle class="van-tyre" cx="712" cy="282" r="30"/><circle class="van-hub" cx="712" cy="282" r="13"/>
    </g>
  </defs>

  <!-- Concept 1: diagonal sweep -->
  <g class="van concept-sweep">
    <use href="#van-outline" class="van-body"/>
    <g clip-path="url(#van-clip)">
      <path class="fill-orange" d="M300,62 L345,62 L400,94 L700,150 L700,170 L380,112 Z"/>
      <path class="fill-navy" d="M186,196 L650,262 L660,280 L186,280 Z"/>
      <path class="fill-orange" d="M186,172 L660,244 L650,262 L186,196 Z"/>
    </g>
    <use href="#van-chassis"/>
    <rect class="fill-orange" x="222" y="92" width="60" height="60"/>
    <text class="website fill-white" x="392" y="106" font-size="10" textLength="160" lengthAdjust="spacingAndGlyphs" transform="rotate(8.5 392 106)">WWW.QUORVELECTRIC.EXAMPLE</text>
    <text class="company-name" x="334" y="158" font-size="22" textLength="250" lengthAdjust="spacingAndGlyphs" transform="rotate(4 334 158)">QUORV ELECTRIC SOLUTION INC</text>
    <line class="rule" x1="334" y1="172" x2="366" y2="175"/>
    <text class="tagline" x="370" y="178" font-size="14" textLength="176" lengthAdjust="spacingAndGlyphs" transform="rotate(5 370 178)">we power your homes</text>
    <line class="rule" x1="550" y1="196" x2="585" y2="200"/>
    <text class="services" x="238" y="192" font-size="9" textLength="300" lengthAdjust="spacingAndGlyphs" transform="rotate(8.5 238 192)">ELECTRICAL REPAIRS • AIR CONDITIONING REPAIR AND INSTALLATION</text>
    <text class="licence fill-white" x="236" y="226" font-size="10">Lic#:2048736</text>
    <text class="phone fill-navy" x="624" y="212" font-size="13" textLength="112" lengthAdjust="spacingAndGlyphs">(555) 482-0173</text>
  </g>

  <!-- Concept 2: horizontal band -->
  <g class="van concept-band" transform="translate(0 297)">
    <use href="#van-outline" class="van-body"/>
    <g clip-path="url(#van-clip)">
      <path class="fill-navy" d="M186,212 L592,212 L620,280 L186,280 Z"/>
      <path class="fill-orange" d="M186,192 L570,192 L600,228 L585,228 L562,206 L186,206 Z"/>
      <path class="fill-orange" d="M604,228 L616,228 L640,280 L628,280 Z"/>
    </g>
    <use href="#van-chassis"/>
    <rect class="fill-orange" x="216" y="96" width="60" height="60"/>
    <text class="website fill-navy" x="372" y="101" font-size="10" textLength="160" lengthAdjust="spacingAndGlyphs">WWW.QUORVELECTRIC.EXAMPLE</text>
    <text class="company-name" x="330" y="146" font-size="22" textLength="250" lengthAdjust="spacingAndGlyphs">QUORV ELECTRIC SOLUTION INC</text>
    <line class="rule" x1="332" y1="163" x2="366" y2="163"/>
    <text class="tagline" x="370" y="167" font-size="14" textLength="178" lengthAdjust="spacingAndGlyphs">we power your homes</text>
    <line class="rule" x1="552" y1="163" x2="586" y2="163"/>
    <text class="services" x="240" y="203" font-size="9" textLength="302" lengthAdjust="spacingAndGlyphs">ELECTRICAL REPAIRS • AIR CONDITIONING REPAIR AND INSTALLATION</text>
    <text class="licence fill-white" x="240" y="227" font-size="10">Lic#:2048736</text>
    <text class="phone fill-navy" x="624" y="227" font-size="13" textLength="112" lengthAdjust="spacingAndGlyphs">(555) 482-0173</text>
  </g>

  <!-- Concept 3: navy cab block -->
  <g class="van concept-cab" transform="translate(0 597)">
    <use href="#van-outline" class="van-body"/>
    <g clip-path="url(#van-clip)">
      <path class="fill-navy" d="M440,60 L800,60 L800,280 L450,280 Z"/>
      <path class="fill-navy" d="M186,192 L436,192 L436,206 L186,206 Z"/>
      <path class="fill-orange" d="M186,206 L436,206 L436,240 L186,240 Z"/>
      <path class="fill-navy" d="M186,240 L440,240 L440,280 L186,280 Z"/>
    </g>
    <use href="#van-chassis"/>
    <rect class="fill-orange" x="470" y="110" width="70" height="70"/>
    <text class="website fill-navy" x="232" y="96" font-size="10" textLength="163" lengthAdjust="spacingAndGlyphs">WWW.QUORVELECTRIC.EXAMPLE</text>
    <text class="company-name" x="210" y="144" font-size="19" textLength="190" lengthAdjust="spacingAndGlyphs">QUORV ELECTRIC SOLUTION INC</text>
    <line class="rule" x1="214" y1="160" x2="240" y2="160"/>
    <text class="tagline" x="243" y="164" font-size="12" textLength="128" lengthAdjust="spacingAndGlyphs">we power your homes</text>
    <line class="rule" x1="375" y1="160" x2="402" y2="160"/>
    <text class="services" x="308" y="202" font-size="7.5" text-anchor="middle" textLength="130" lengthAdjust="spacingAndGlyphs">ELECTRICAL REPAIRS AIR CONDITIONING</text>
    <text class="services" x="308" y="213" font-size="7.5" text-anchor="middle" textLength="90" lengthAdjust="spacingAndGlyphs">REPAIR AND INSTALLATION</text>
    <text class="licence fill-navy" x="212" y="230" font-size="10">Lic#:2048736</text>
    <text class="phone fill-white" x="620" y="218" font-size="13" textLength="112" lengthAdjust="spacingAndGlyphs">(555) 482-0173</text>
  </g>
</svg>
</body>
</html>
```